Vormex Business Card

We are a security company in Central Aus, we supply guards, patrols, alarm monitoring, cash in transit, major event security.

I would like a modern card, possibly matte finish with gloss logo.... up for anything really

Our business colors are black white and blue.

on the back side of the card i was thinking having our logo just centered or our slogan ( "Securing Your Territory 24/7" )

Industry/Entity Type

Security

Contact Information for Business Card

Company Name: Vormex Security Service
My Name: Gareth Pelling
Position: Director
Mobil: 0452 918 307
Work: 89 612 734
Fax: 89 61 48 23
Email: gary.pelling@vormex.com.au
web: vormex.com.au
Address: 14 Brindle Road Marrow Creek NT 0894

```html
<!DOCTYPE html>
<html lang="en">
<head>
<meta charset="utf-8">
<title>Vormex Security Service – Business Card</title>
<link rel="stylesheet" href="https://fonts.googleapis.com/css2?family=Exo+2:wght@400;600;700&display=swap">
<style>
  :root {
    --page-bg: #e4e5e7;
    --brand-blue: #4a86c6;
    --brand-blue-deep: #3a6fb0;
    --brand-blue-light: #6aa2d8;
    --card-white: #f4f5f6;
    --ink: #1a1a1a;
    --divider: #4a86c6;
    --font-main: "Exo 2", Arial, sans-serif;
  }
  * { box-sizing: border-box; margin: 0; padding: 0; }
  html, body {
    width: 1200px;
    height: 750px;
    overflow: hidden;
    background: var(--page-bg);
    font-family: var(--font-main);
  }
  .canvas {
    width: 1200px;
    height: 750px;
    display: flex;
    align-items: center;
    justify-content: center;
    gap: 60px;
  }
  .card {
    position: relative;
    width: 520px;
    height: 297px;
    border-radius: 24px;
    overflow: hidden;
    box-shadow: 0 6px 18px rgba(0, 0, 0, 0.18);
  }

  /* Back side */
  .card-back {
    background: linear-gradient(135deg, var(--brand-blue-light), var(--brand-blue-deep));
    display: flex;
    align-items: center;
    justify-content: center;
  }
  .back-name {
    color: #eef4fb;
    font-weight: 700;
    font-size: 64px;
    letter-spacing: 6px;
    text-transform: uppercase;
  }

  /* Front side */
  .card-front { background: var(--card-white); }
  .front-band {
    position: absolute;
    inset: 0;
    width: 100%;
    height: 100%;
  }
  .front-brand {
    position: absolute;
    left: 28px;
    top: 150px;
    width: 200px;
    color: var(--brand-blue);
    font-weight: 700;
    line-height: 1.05;
    text-transform: uppercase;
  }
  .front-brand .brand-word { display: block; font-size: 44px; letter-spacing: 3px; }
  .front-brand .brand-sub { display: block; font-size: 18px; letter-spacing: 2px; margin-top: 4px; }
  .front-divider {
    position: absolute;
    left: 236px;
    top: 92px;
    width: 2px;
    height: 170px;
    background: var(--divider);
  }
  .contact {
    position: absolute;
    left: 252px;
    top: 90px;
    color: var(--brand-blue);
    font-size: 15px;
    line-height: 1.3;
  }
  .contact-name { font-weight: 700; font-size: 19px; }
  .contact-role { color: var(--ink); font-size: 14px; margin-bottom: 2px; }
  .contact-row { display: flex; align-items: center; gap: 7px; }
  .contact-row .spacer { width: 14px; flex: none; }
  .icon { width: 14px; height: 14px; flex: none; }
  .contact-address { padding-left: 21px; margin-top: -1px; }
</style>
</head>
<body>
<main class="canvas">

  <section class="card card-back" aria-label="Card back">
    <span class="back-name">Vormex</span>
  </section>

  <section class="card card-front" aria-label="Card front">
    <svg class="front-band" viewBox="0 0 520 297" preserveAspectRatio="none" aria-hidden="true">
      <defs>
        <linearGradient id="bandFill" x1="0" y1="0" x2="1" y2="1">
          <stop offset="0" stop-color="#6aa2d8"/>
          <stop offset="1" stop-color="#3a6fb0"/>
        </linearGradient>
      </defs>
      <path d="M0 0 H520 V18 C420 20 300 70 200 110 C120 140 50 150 0 150 Z" fill="url(#bandFill)"/>
    </svg>

    <div class="front-brand">
      <span class="brand-word">Vormex</span>
      <span class="brand-sub">Security Service</span>
    </div>

    <div class="front-divider"></div>

    <div class="contact">
      <div class="contact-name">Gareth Pelling</div>
      <div class="contact-role">director</div>
      <div class="contact-row"><span class="spacer"></span>0452 918 307</div>
      <div class="contact-row"><span class="spacer"></span>89 612 734</div>
      <div class="contact-row">
        <svg class="icon" viewBox="0 0 14 14" aria-label="Fax"><circle cx="7" cy="7" r="7" fill="#1a1a1a"/><path d="M4.3 3.6c.5-.4 1-.3 1.2.1l.6 1.2c.2.4 0 .7-.3 1l-.3.3c.3.8.9 1.4 1.7 1.7l.3-.3c.3-.3.6-.5 1-.3l1.2.6c.4.2.5.7.1 1.2-.6.7-1.4.9-2.3.5-1.5-.7-2.5-1.7-3.2-3.2-.4-.9-.2-1.700.5-2.3z" fill="#fff"/></svg>
        89 61 48 23
      </div>
      <div class="contact-row">
        <svg class="icon" viewBox="0 0 14 14" aria-label="Email"><circle cx="7" cy="7" r="7" fill="#1a1a1a"/><rect x="3.5" y="4.5" width="7" height="5" fill="none" stroke="#fff" stroke-width="1"/><path d="M3.5 4.5 7 7.3 10.5 4.5" fill="none" stroke="#fff" stroke-width="1"/></svg>
        gary.pelling@vormex.com.au
      </div>
      <div class="contact-row">
        <svg class="icon" viewBox="0 0 14 14" aria-label="Website"><circle cx="7" cy="7" r="7" fill="#1a1a1a"/><circle cx="7" cy="7" r="3.6" fill="none" stroke="#fff" stroke-width="1"/><path d="M3.4 7h7.2M7 3.4c-1.6 2-1.6 5.2 0 7.2M7 3.4c1.6 2 1.6 5.2 0 7.2" fill="none" stroke="#fff" stroke-width=".8"/></svg>
        www.vormex.com.au
      </div>
      <div class="contact-row">
        <svg class="icon" viewBox="0 0 14 14" aria-label="Address"><circle cx="7" cy="7" r="7" fill="#1a1a1a"/><path d="M7 3a2.6 2.6 0 0 0-2.6 2.6C4.4 7.6 7 11 7 11s2.6-3.4 2.6-5.4A2.6 2.6 0 0 0 7 3z" fill="#fff"/><circle cx="7" cy="5.6" r="1" fill="#1a1a1a"/></svg>
        14 Brindle Road Marrow
      </div>
      <div class="contact-address">Creek NT 0894</div>
    </div>
  </section>

</main>
</body>
</html>
```